Duel Business card

Want an edgy business card that shows both of our companies on each side of the card, OR both together with a cool design.

*Must be edgy: We have attached our two business logos. We are a bail bond and immigration bond company.

Would like the address on one side only.
Need Phone, cell, website, address, and Name

Company Name 1: Cellgate Release Partners
www.cellgatereleasepartners.example

Company Name 2: Borderline Surety Associates
www.borderlinesuretyassociates.example

These cards will need to be easily changeable so I can modify new employees

Target Market(s)

people in jail, takign imigrants out of jail and from being taken back to there country

Industry/Entity Type

Business

Requirements
Must have
• Include both logos attached

```html
<!DOCTYPE html>
<html lang="en">
<head>
<meta charset="utf-8">
<title>Business Card – Cellgate Release Partners &amp; Borderline Surety Associates</title>
<link href="https://fonts.googleapis.com/css2?family=Roboto:wght@400;700&display=swap" rel="stylesheet">
<style>
  :root {
    --navy: #1d3a63;
    --blue-name: #1f5b8e;
    --gold: #ecbb2e;
    --ink: #333b44;
    --rule: #8a8f96;
    --paper: #ffffff;
    --stage: #ffffff;
  }
  * { box-sizing: border-box; margin: 0; padding: 0; }
  html, body {
    width: 1200px; height: 900px; overflow: hidden;
    background: var(--stage);
    font-family: "Roboto", Arial, sans-serif;
  }
  .canvas { position: relative; width: 1200px; height: 900px; }

  .card {
    position: absolute; left: 293px; width: 616px; height: 353px;
    background: var(--paper);
    box-shadow: 5px 6px 8px rgba(0,0,0,0.35);
    overflow: hidden;
  }
  .card--front { top: 67px; }
  .card--back { top: 480px; }

  .card__band { position: absolute; left: 0; bottom: 0; width: 616px; height: 19px; display: block; }

  .brand {
    position: absolute; display: flex; flex-direction: column; align-items: center;
    text-align: center; transform: translateX(-50%);
  }
  .brand__dot { width: 58px; height: 58px; border-radius: 50%; margin-bottom: 8px; }
  .brand__dot--navy { background: var(--navy); }
  .brand__dot--gold { background: var(--gold); }
  .brand__name {
    color: var(--navy); font-weight: 700; font-size: 19px; line-height: 1.15;
    text-transform: uppercase; letter-spacing: 0.5px;
  }
  .brand__site { margin-top: 12px; color: var(--ink); font-size: 14px; white-space: nowrap; }

  .front-brand-1 { left: 147px; top: 42px; }
  .front-brand-2 { left: 147px; top: 178px; }
  .front-brand-1 .brand__dot, .front-brand-2 .brand__dot { width: 44px; height: 44px; margin-bottom: 6px; }
  .front-brand-1 .brand__name, .front-brand-2 .brand__name { font-size: 16px; }

  .back-brand-1 { left: 174px; top: 105px; }
  .back-brand-2 { left: 458px; top: 105px; }

  .card__divider {
    position: absolute; left: 307px; top: 84px; width: 1px; height: 186px;
    background: linear-gradient(to bottom, transparent, var(--rule) 20%, var(--rule) 80%, transparent);
  }

  .contact { position: absolute; left: 360px; top: 102px; color: var(--ink); font-size: 15px; }
  .contact__name { color: var(--blue-name); font-weight: 700; font-size: 21px; line-height: 1.2; }
  .contact__title { margin-top: 4px; }
  .contact__address { margin-top: 22px; line-height: 20px; }
  .contact__phones { margin-top: 4px; list-style: none; line-height: 20px; }
  .contact__phones li { display: flex; align-items: center; gap: 6px; }
  .contact__icon { width: 14px; height: 14px; flex: none; }
</style>
</head>
<body>
<main class="canvas">

  <section class="card card--front" aria-label="Card front">
    <div class="brand front-brand-1">
      <span class="brand__dot brand__dot--navy"></span>
      <span class="brand__name">Borderline Surety<br>Associates</span>
    </div>
    <div class="brand front-brand-2">
      <span class="brand__dot brand__dot--gold"></span>
      <span class="brand__name">Cellgate Release<br>Partners</span>
    </div>

    <div class="card__divider"></div>

    <div class="contact">
      <p class="contact__name">Daniel Whitford</p>
      <p class="contact__title">Founder &amp; CEO</p>
      <p class="contact__address">4417 Harrowgate Lane<br>Brookfield, VA 20199</p>
      <ul class="contact__phones">
        <li>
          <svg class="contact__icon" viewBox="0 0 14 14" aria-label="Phone">
            <circle cx="7" cy="7" r="7" fill="var(--blue-name)"/>
            <path d="M4.6 3.4l1.3 1.6-.7.9c.5 1.1 1.3 1.9 2.4 2.4l.9-.7 1.6 1.3-.8 1.2C6.6 9.9 4.1 7.4 3.4 4.2z" fill="#fff"/>
          </svg>
          (555) 214-7730
        </li>
        <li>
          <svg class="contact__icon" viewBox="0 0 14 14" aria-label="Cell">
            <circle cx="7" cy="7" r="7" fill="var(--blue-name)"/>
            <rect x="4.6" y="2.8" width="4.8" height="8.4" rx="1" fill="#fff"/>
            <rect x="5.4" y="3.8" width="3.2" height="5.4" fill="var(--blue-name)"/>
          </svg>
          (555) 214-7730
        </li>
      </ul>
    </div>

    <svg class="card__band" viewBox="0 0 616 19" preserveAspectRatio="none" aria-hidden="true">
      <polygon points="0,0 320,0 312,19 0,19" fill="var(--navy)"/>
      <polygon points="320,0 616,0 616,19 312,19" fill="var(--gold)"/>
    </svg>
  </section>

  <section class="card card--back" aria-label="Card back">
    <div class="brand back-brand-1">
      <span class="brand__dot brand__dot--navy"></span>
      <span class="brand__name">Borderline Surety<br>Associates</span>
      <span class="brand__site">www.borderlinesuretyassociates.example</span>
    </div>
    <div class="brand back-brand-2">
      <span class="brand__dot brand__dot--gold"></span>
      <span class="brand__name">Cellgate Release<br>Partners</span>
      <span class="brand__site">www.cellgatereleasepartners.example</span>
    </div>

    <svg class="card__band" viewBox="0 0 616 19" preserveAspectRatio="none" aria-hidden="true">
      <polygon points="0,0 320,0 312,19 0,19" fill="var(--navy)"/>
      <polygon points="320,0 616,0 616,19 312,19" fill="var(--gold)"/>
    </svg>
  </section>

</main>
</body>
</html>
```